New Wix Website Design Project For New Finance Company

Create new design for a new page. Website should match existing theme of presentation deck, business card and logo attached to the brief. The site will have five pages

1) Home
2) Investment Criteria
3) Approach
4) Team
5) Contact

Some examples include
http://www.bluemaplefunds.com/

Although not a requirement, if the below white fence or similar could be added subtly to the sight as well, that would be great.

https://www.searvok.com/search?q=white+fence+horse&rlz=7K4TTPM_enUS218US264&source=lnms&tbm=isch&sa=X&ved=0bhVKEwqxmbtnyLvgBhWE3oNKHVtsBF4Q_BUIDyhD&biw=1920&bih=958#imgrc=vkd2PQx47eMLTA:

Target Market(s)

Business Professionals

Font styles to use
Sans Serif

Colors

Designer to choose colors to be used in the design.

Requirements
Must have
• Clean layout. Easy to upload header and footer.

```html
<!DOCTYPE html>
<html lang="en">
<head>
<meta charset="utf-8">
<title>Ridge Hollow Capital</title>
<link rel="stylesheet" href="https://fonts.googleapis.com/css2?family=Montserrat:wght@600;700&display=swap">
<style>
  :root {
    --brand-blue: #1b72c2;
    --nav-blue: #1c5f9e;
    --page-white: #ffffff;
    --sky-cream: #f7f3ee;
    --glass-teal: #5fa3ad;
    --glass-pale: #c9e0ea;
    --glass-deep: #2f6f80;
  }
  * { margin: 0; padding: 0; box-sizing: border-box; }
  html, body {
    width: 1200px;
    height: 900px;
    overflow: hidden;
    background: var(--page-white);
    font-family: "Montserrat", Arial, sans-serif;
  }
  .site-header {
    height: 70px;
    display: flex;
    align-items: center;
    justify-content: space-between;
    padding: 0 139px 0 137px;
    background: var(--page-white);
  }
  .brand-name {
    color: var(--brand-blue);
    font-weight: 700;
    font-size: 20px;
    letter-spacing: 0.5px;
    text-transform: uppercase;
    text-decoration: none;
  }
  .main-nav {
    display: flex;
    gap: 29px;
    list-style: none;
  }
  .main-nav a {
    color: var(--nav-blue);
    font-weight: 600;
    font-size: 11.5px;
    text-decoration: none;
    text-transform: uppercase;
  }
  .hero {
    position: relative;
    height: 830px;
    display: flex;
    align-items: center;
    justify-content: center;
    overflow: hidden;
  }
  .hero-photo {
    position: absolute;
    inset: 0;
    background:
      linear-gradient(135deg, transparent 55%, var(--glass-teal) 56%, var(--glass-deep) 100%),
      linear-gradient(225deg, transparent 70%, var(--glass-pale) 71%),
      linear-gradient(0deg, var(--glass-pale) 0%, transparent 35%),
      var(--sky-cream);
  }
  .hero-title {
    position: relative;
    margin-top: -20px;
    color: var(--brand-blue);
    font-weight: 700;
    font-size: 62px;
    letter-spacing: 1px;
    text-transform: uppercase;
    text-align: center;
  }
</style>
</head>
<body>
  <header class="site-header">
    <a class="brand-name" href="#">Ridge Hollow Capital</a>
    <nav>
      <ul class="main-nav">
        <li><a href="#">Home</a></li>
        <li><a href="#">Investment Criteria</a></li>
        <li><a href="#">Approach</a></li>
        <li><a href="#">Team</a></li>
        <li><a href="#">Contact</a></li>
      </ul>
    </nav>
  </header>
  <main class="hero">
    <div class="hero-photo" role="img" aria-label="Upward view of glass office towers against a pale sky"></div>
    <h1 class="hero-title">Ridge Hollow Capital</h1>
  </main>
</body>
</html>
```